ROB & JO’S GOODBYE TO MIDGE BITES

I require an attractive appealing label with the dimensions 7.5m x 3.5cm
This is a Natural sandfly insect repellent cream formulated by 2 pharmacists Carla Whitby and Rob Kettering. It is required for labelling a 50 g jar

Contains Essential Oils of cedar wood, rosemary, cinnamon, citronella, lavender, eucalyptus and clove in a moisturising base.

We would like to see designs using the colour bright duck egg blue as the main colour with dark brown tones for the patterns. An eye catching label is output aim . However any colour combination that is attractive to the eye is welcome
A gloss finish is preferable.

More designs please

Target Market(s)

Trekkers, outdoor active people, pharmacy, health shops

Colors
abd037
34a6d7
0456a4
33b8a4

Requirements
Must have
• Rob and Jo’s
• Goodbye to Midge bites
• Natural Sandfly Repellent
• Contains Essential Oils of cedar wood, rosemary, cinnamon, citronella, lavender, eucalyptus and clove in a moisturising base.
• Formulated by Australian Pharmacists Carla Whitby and Rob Kettering
• Made in Australia
• 0413862207
Nice to have
• Sandfly/ flies
• I have attached a label I use for my mozzie cream and would like a similar font please

```html
<!DOCTYPE html>
<html lang="en">
<head>
<meta charset="utf-8">
<title>Rob and Jo’s Goodbye to Midge Bites – Jar Label</title>
<link rel="stylesheet" href="https://fonts.googleapis.com/css2?family=Open+Sans:wght@600;700&family=Pinyon+Script&display=swap">
<style>
  :root {
    --page: #e4e4e4;
    --duck-egg: #8fdbe0;
    --duck-egg-light: #d3f1ef;
    --duck-egg-deep: #6fcad6;
    --brown: #4b2a2b;
    --brown-deep: #3a1f20;
    --olive: #5d5a26;
    --olive-dark: #4e4b20;
    --ink: #3b3b3b;
    --white: #ffffff;
    --mint: #c6efdc;
    --amber: #c9a24a;
  }
  * { box-sizing: border-box; margin: 0; padding: 0; }
  html, body { width: 810px; height: 1200px; overflow: hidden; }
  body {
    background: var(--page);
    font-family: "Open Sans", Arial, sans-serif;
    position: relative;
  }

  /* Hang tag */
  .hang-tag {
    position: absolute;
    left: 285px; top: 150px;
    width: 240px; height: 200px;
    background: var(--mint);
    border-radius: 18px;
  }
  .hang-tag__hole {
    position: absolute; left: 108px; top: 18px;
    width: 24px; height: 24px; border-radius: 50%;
    background: var(--page);
  }
  .hang-tag__owner {
    position: absolute; left: 0; right: 0; top: 70px;
    text-align: center; font-weight: 700; font-size: 24px; color: var(--brown);
  }
  .hang-tag__brand {
    position: absolute; left: 0; right: 0; top: 104px;
    text-align: center; font-weight: 700; font-size: 56px; color: var(--olive);
    letter-spacing: 2px;
  }

  /* Label */
  .label {
    position: absolute;
    left: 25px; top: 430px;
    width: 760px; height: 440px;
    background: linear-gradient(100deg, var(--duck-egg-deep) 0%, var(--duck-egg) 35%, var(--duck-egg-light) 75%, var(--duck-egg) 100%);
    overflow: hidden;
  }
  .label__swoosh { position: absolute; left: 0; top: 0; width: 760px; height: 60px; }
  .label__fly-corner {
    position: absolute; right: 10px; top: 14px;
    width: 40px; height: 40px; border-radius: 50%;
    background: radial-gradient(circle, var(--amber), #8a6a2a);
  }
  .label__owner {
    position: absolute; left: 16px; top: 62px;
    font-size: 34px; font-weight: 700; color: var(--ink);
  }
  .label__brand {
    position: absolute; left: 80px; top: 100px;
    font-size: 104px; font-weight: 700; line-height: 1; color: var(--olive);
    letter-spacing: 4px;
  }
  .label__product-bar {
    position: absolute; left: 40px; top: 245px;
    width: 440px; height: 46px;
    background: var(--brown-deep);
    color: var(--white); font-weight: 700; font-size: 27px;
    line-height: 46px; padding-left: 46px;
  }
  .label__fly-badge {
    position: absolute; left: 10px; top: 238px;
    width: 60px; height: 60px; border-radius: 50%;
    background: radial-gradient(circle, var(--amber) 0 40%, var(--white) 42% 70%, var(--brown-deep) 72%);
  }
  .label__tagline {
    position: absolute; font-family: "Pinyon Script", cursive; color: var(--ink);
  }
  .label__tagline--natural { left: 455px; top: 70px; font-size: 42px; transform: rotate(-12deg); }
  .label__tagline--type { left: 385px; top: 130px; font-size: 44px; transform: rotate(-14deg); }
  .label__origin {
    position: absolute; left: 560px; top: 212px;
    transform: rotate(12deg); text-align: center;
  }
  .label__origin-text { font-weight: 700; font-size: 20px; color: var(--olive-dark); }
  .label__phone {
    margin-top: 2px; display: inline-block;
    background: var(--olive-dark); color: var(--white);
    font-weight: 700; font-size: 21px;
    padding: 4px 20px; border-radius: 50%;
  }
  .label__credit {
    position: absolute; left: 0; right: 0; top: 308px;
    text-align: center; font-weight: 700; font-size: 19px; color: var(--ink);
    padding-left: 20px;
  }
  .label__ingredients {
    position: absolute; left: 0; bottom: 0;
    width: 760px; height: 100px;
    background: var(--brown);
    color: var(--white); font-weight: 700; font-size: 20px; line-height: 1.4;
    text-align: center; padding: 18px 10px 0;
  }
</style>
</head>
<body>

  <div class="hang-tag">
    <span class="hang-tag__hole"></span>
    <p class="hang-tag__owner">Rob and Jo’s</p>
    <p class="hang-tag__brand">GMB</p>
  </div>

  <section class="label">
    <svg class="label__swoosh" viewBox="0 0 760 60" aria-hidden="true">
      <path d="M0 0 H760 V40 C520 8 260 8 0 32 Z" fill="var(--brown)"/>
      <path d="M0 34 C260 10 520 10 760 42" stroke="var(--white)" stroke-width="5" fill="none"/>
      <path d="M0 42 C260 18 520 18 760 50" stroke="var(--olive)" stroke-width="5" fill="none"/>
    </svg>
    <div class="label__fly-corner" role="img" aria-label="Small sandfly illustration"></div>

    <p class="label__owner">Rob and Jo’s</p>
    <p class="label__brand">GMB</p>

    <p class="label__tagline label__tagline--natural">Natural</p>
    <p class="label__tagline label__tagline--type">Sandfly Repellent</p>

    <div class="label__product-bar">GOODBYE TO MIDGE BITES</div>
    <div class="label__fly-badge" role="img" aria-label="Sandfly illustration in a round badge"></div>

    <div class="label__origin">
      <p class="label__origin-text">Made in Australia</p>
      <p class="label__phone">0413862207</p>
    </div>

    <p class="label__credit">Formulated by Australian Pharmacists Carla Whitby and Rob Kettering</p>

    <p class="label__ingredients">Contains Essential Oils of cedar wood, rosemary, cinnamon, citronella,<br>lavender, eucalyptus and clove in a moisturising base.</p>
  </section>

</body>
</html>
```